Torquel Australia Pty Ltd

I require professional business cards with our company logo. We would like something that looks sharp and unique. I have attached the logo for our business, which is an industrial electrical contracting company. But this does not need to be shown on the cards.

Industry/Entity Type

Industrial

Requirements
Must have
• The design must be double sided and needs to have one side with our logo only and the other side with our details.
Should not have
• We do not want any lightening bolts on the designs as this is very common.

```html
<!DOCTYPE html>
<html lang="en">
<head>
<meta charset="utf-8">
<title>Torquel Australia Pty Ltd — Business Card</title>
<link rel="stylesheet" href="https://fonts.googleapis.com/css2?family=Open+Sans:ital,wght@0,400;0,600;1,400&display=swap">
<style>
  :root {
    --backdrop: #c9ccc8;
    --card: #f4f4f4;
    --card-edge: #e2e2e2;
    --ink: #3a3a3a;
    --ink-soft: #555555;
    --rule: #8a8a8a;
    --watermark: #e3e3e3;
  }
  * { margin: 0; padding: 0; box-sizing: border-box; }
  html, body {
    width: 1200px; height: 1000px; overflow: hidden;
    background: var(--backdrop);
    font-family: "Open Sans", Arial, sans-serif;
    color: var(--ink);
  }
  .sheet {
    width: 1200px; height: 1000px;
    display: flex; flex-direction: column;
    align-items: center; justify-content: center; gap: 50px;
  }
  .card {
    position: relative;
    width: 680px; height: 415px;
    background: linear-gradient(135deg, #fafafa 0%, var(--card) 55%, var(--card-edge) 100%);
    box-shadow: 0 6px 18px rgba(0,0,0,0.18);
    overflow: hidden;
  }
  .watermark {
    position: absolute; right: -70px; top: 50%;
    transform: translateY(-50%);
    width: 360px; height: 360px;
  }
  .wordmark {
    position: relative;
    display: flex; align-items: center; gap: 18px;
  }
  .wordmark-dot {
    flex: none; border-radius: 50%;
    border: 9px solid var(--ink);
  }
  .wordmark-name {
    font-weight: 600; color: var(--ink);
    text-transform: uppercase; line-height: 1;
  }
  .wordmark-name span { display: block; }

  /* Logo side */
  .card--front .wordmark { position: absolute; left: 84px; top: 150px; }
  .card--front .wordmark-dot { width: 110px; height: 110px; }
  .card--front .wordmark-name .line-main { font-size: 64px; letter-spacing: 2px; }
  .card--front .wordmark-name .line-sub { font-size: 22px; letter-spacing: 9px; margin-top: 8px; }

  /* Details side */
  .card--back .wordmark { position: absolute; left: 34px; top: 34px; gap: 10px; }
  .card--back .wordmark-dot { width: 58px; height: 58px; border-width: 5px; }
  .card--back .wordmark-name .line-main { font-size: 34px; letter-spacing: 1px; }
  .card--back .wordmark-name .line-sub { font-size: 12px; letter-spacing: 5px; margin-top: 4px; }

  .person { position: absolute; left: 96px; top: 130px; }
  .person-name { font-size: 20px; color: var(--ink-soft); }
  .person-role { font-size: 13px; font-style: italic; color: var(--ink-soft); margin-top: 2px; }

  .divider {
    position: absolute; left: 26px; right: 26px; top: 198px;
    height: 1px; background: var(--rule);
  }
  .details { position: absolute; font-size: 14px; line-height: 1.35; color: var(--ink-soft); }
  .details--postal { left: 96px; top: 210px; }
  .details--contact { left: 400px; top: 238px; }
</style>
</head>
<body>
<main class="sheet">

  <section class="card card--front" aria-label="Business card, logo side">
    <svg class="watermark" viewBox="0 0 100 100" aria-hidden="true">
      <circle cx="50" cy="50" r="44" fill="none" stroke="var(--watermark)" stroke-width="9"/>
    </svg>
    <div class="wordmark">
      <div class="wordmark-dot"></div>
      <div class="wordmark-name">
        <span class="line-main">Torquel</span>
        <span class="line-sub">Australia Pty Ltd</span>
      </div>
    </div>
  </section>

  <section class="card card--back" aria-label="Business card, details side">
    <svg class="watermark" viewBox="0 0 100 100" aria-hidden="true">
      <circle cx="50" cy="50" r="44" fill="none" stroke="var(--watermark)" stroke-width="9"/>
    </svg>
    <div class="wordmark">
      <div class="wordmark-dot"></div>
      <div class="wordmark-name">
        <span class="line-main">Torquel</span>
        <span class="line-sub">Australia Pty Ltd</span>
      </div>
    </div>
    <div class="person">
      <p class="person-name">Reuben Hale</p>
      <p class="person-role">Director</p>
    </div>
    <div class="divider"></div>
    <div class="details details--postal">
      <p>Address: PO Box 318 Kelvale</p>
      <p>NSW 2590</p>
      <p>Phone: 02 5550 1847</p>
    </div>
    <div class="details details--contact">
      <p>Mobile: 0400 555 219</p>
      <p>Email: reuben@torquelaustralia.com.au</p>
      <p>www.torquelaustralia.com.au</p>
    </div>
  </section>

</main>
</body>
</html>
```